Website Redesign for InkForgeHub.co.za – Bold, Modern & Professional Tattoo Supply Store (B2B ...

PLEASE DO NOT CONTACT US OUTSIDE PIXELHARBOR.COM

We’re looking for a skilled and creative web designer to redesign InkForgeHub.co.za, a leading tattoo equipment and supplies store based in South Africa. The business serves both B2B (tattoo studios, artists, wholesalers) and B2C (individual customers) markets.

The current website is outdated and lacks the modern, edgy look that reflects the tattoo industry. We want a fresh, bold, and professional design that appeals to both professional artists and retail customers — combining trust, style, and functionality.

About the Business:
Inkforge Hub supplies a wide range of tattoo-related products, including machines, needles, inks, hygiene supplies, and accessories. The company is well-established in the South African market and serves both individual tattoo artists and studios, as well as end customers looking for quality equipment.

The website must reflect the creative, bold, and artistic nature of the tattoo industry, while still being easy to navigate, fast, and conversion-focused.

What We’re Looking For:
A bold, modern design with a clear structure
Strong visual identity that reflects the tattoo culture — edgy, artistic, but still clean and professional
A layout that works for both B2B and B2C audiences
Clear product presentation and strong CTAs (Buy Now, Request Quote, Contact, etc.)
Fully responsive design (desktop + mobile)
Easy-to-navigate product categories and filters
Space for featured products, promotions, and artist-focused content
Integration of trust elements (payment icons, reviews, certifications, etc.)

Pages We Need Designed:
Homepage
Product detail page

Inspiration / Style Direction:
We’re looking for something with a strong personality, inspired by tattoo culture, but still clean and user-friendly. Think:

Dark theme with bold highlights (but open to light themes if well executed)
High-quality visuals and product imagery

Examples for inspiration:
GlowNeedle.co.uk
Pellman QRV
Garnet Tattoo Supply
Velvet Salve

Deliverables:
Full desktop and mobile designs (Figma, XD, or PSD)
All design source files
Fonts, icons, and assets used
Clearly labeled layers and organized files
Ready for development handoff

Target Market(s)

InkForgeHub.co.za targets both B2B and B2C customers in South Africa: B2B: Professional tattoo artists, studios, and wholesalers looking for high-quality, reliable equipment and bulk pricing. B2C: Individual customers, hobbyists, and beginners seeking safe, affordable tattoo supplies with guidance and support. The site should appeal to both experienced professionals and newcomers, combining a bold, authentic tattoo vibe with a clean, user-friendly shopping experience.

Industry/Entity Type

Tattoo Equipment & Supplies – E-commerce (B2B & B2C)

Number of Pages Required

2 page

Requirements
Must have
• Responsive design, bold tattoo-inspired visual style, clear navigation for B2B & B2C, strong product presentation, clear call-to-actions, trust elements (reviews, badges, payment icons), category filters & search, dedicated B2B/wholesale info page, speed-optimized layout, easy access to contact & support.
Should not have
• Overly complex animations, cluttered layout, generic stock images, too many fonts or colors, hidden navigation, auto-play videos or sounds, outdated visual styles, low-quality product images, confusing checkout process, unnecessary pop-ups.

```html
<!DOCTYPE html>
<html lang="en">
<head>
<meta charset="utf-8">
<title>Inkforge Hub – Professional Tattoo Equipment &amp; Supplies</title>
<link href="https://fonts.googleapis.com/css2?family=Cinzel:wght@500;600;700&family=Outfit:wght@300;400;500;600&display=swap" rel="stylesheet">
<style>
:root{
  --bg:#0f0f0f;
  --header:#121212;
  --nav:#171717;
  --strip:#1d1d1d;
  --card:#141414;
  --line:#2c2c2c;
  --text:#ffffff;
  --green:#3fb54d;
  --star:#f2a516;
}
*{box-sizing:border-box;margin:0;padding:0}
html,body{width:1200px;height:3743px;overflow:hidden;background:var(--bg);color:var(--text);font-family:"Outfit",sans-serif}
.page{position:relative;width:1200px;height:3743px;overflow:hidden}
.abs{position:absolute}
section,header,footer,nav{position:absolute;left:0;width:1200px;overflow:hidden}

.site-header{top:0;height:84px;background:var(--header)}
.brand{left:144px;top:28px;display:flex;align-items:center;gap:8px;font-weight:600;font-size:19px;letter-spacing:1px}
.brand .mark{width:14px;height:14px;background:var(--text)}
.search{left:447px;top:25px;width:324px;height:35px;border:1px solid #333;border-radius:3px;background:#161616;font-size:12px;color:#6d6d6d;padding:9px 14px}
.search svg{position:absolute;right:12px;top:10px}
.account{left:808px;top:34px;font-size:13px;display:flex;gap:7px;align-items:center}
.cart-info{left:915px;top:35px;font-size:12px;color:#fff}
.cart-btn{left:1027px;top:27px;width:31px;height:31px;border-radius:50%;background:var(--green);display:flex;align-items:center;justify-content:center}

.main-nav{top:84px;height:43px;background:var(--nav);border-top:1px solid #222}
.main-nav a{position:absolute;top:14px;font-size:12.5px;color:#d6d6d6;text-decoration:none}
.main-nav a.active{color:#fff;font-weight:500}

.hero{top:127px;height:579px;background:
  radial-gradient(ellipse 16% 20% at 67% 30%,#9a7a3e 0%,rgba(154,122,62,0) 100%),
  radial-gradient(ellipse 45% 40% at 92% 75%,#4b4a78 0%,rgba(75,74,120,0) 100%),
  radial-gradient(ellipse 35% 45% at 65% 40%,#5d5f66 0%,rgba(60,62,68,0) 100%),
  linear-gradient(100deg,#1a1b1e 0%,#2c2e33 45%,#3c3e44 70%,#2a2b33 100%)}
.hero-photo{position:absolute;inset:0;background:linear-gradient(100deg,rgba(10,10,10,.75) 0%,rgba(15,15,15,.35) 45%,rgba(0,0,0,0) 70%)}
.hero h1{position:absolute;left:144px;top:112px;font-family:"Cinzel",serif;font-weight:500;font-size:44px;line-height:66px;font-variant:small-caps}
.hero h1 .b{font-weight:700}
.hero p{position:absolute;left:144px;top:314px;font-size:16.5px;line-height:31px;color:#eaeaea;font-weight:300}
.btn{position:absolute;display:flex;align-items:center;justify-content:center;font-size:15px;border-radius:2px}
.btn-green{background:var(--green)}
.btn-ghost{border:1.5px solid #d8d8d8}

.section-title{position:absolute;left:0;width:1200px;text-align:center;font-family:"Cinzel",serif;font-weight:700;font-size:29px;font-variant:small-caps}
.section-sub{position:absolute;left:0;width:1200px;text-align:center;font-size:13px;color:#dcdcdc;font-weight:300}

/* product photo tones */
.tone-caps{background:radial-gradient(ellipse 38% 30% at 50% 55%,#1e1e1e 0%,#3a3a3a 50%,rgba(255,255,255,0) 100%),#fff}
.tone-purple{background:radial-gradient(ellipse 10% 42% at 50% 50%,#3b3d9c 0%,#5f62b8 55%,rgba(255,255,255,0) 100%),#fff}
.tone-black{background:radial-gradient(ellipse 10% 42% at 50% 52%,#111 0%,#2a2a2a 55%,rgba(255,255,255,0) 100%),#fff}
.tone-ink-box{background:radial-gradient(ellipse 26% 40% at 52% 50%,#111 0%,#2b2b2b 60%,rgba(255,255,255,0) 100%),#fff}
.tone-blue{background:radial-gradient(ellipse 20% 40% at 50% 50%,#8fc7ea 0%,#bfe0f4 55%,rgba(255,255,255,0) 100%),#fff}
.tone-red{background:radial-gradient(ellipse 18% 22% at 60% 45%,#e44b33 0%,rgba(228,75,51,0) 100%),radial-gradient(ellipse 14% 16% at 40% 55%,#222 0%,rgba(34,34,34,0) 100%),#fff}
.tone-silver{background:radial-gradient(ellipse 24% 40% at 50% 55%,#8c8c8c 0%,#c4c4c4 55%,rgba(255,255,255,0) 100%),#fff}
.tone-cups{background:radial-gradient(ellipse 45% 35% at 40% 55%,#d8d8d8 0%,#ececec 60%,rgba(255,255,255,0) 100%),linear-gradient(90deg,#cfcfcf,#fff)}
.tone-stand{background:radial-gradient(ellipse 20% 40% at 55% 50%,#2a2a2a 0%,#5a5a5a 50%,rgba(255,255,255,0) 100%),linear-gradient(90deg,#ffffff,#d0d0d0)}
.edge-left{-webkit-mask-image:linear-gradient(90deg,rgba(0,0,0,.7),#000 60%);mask-image:linear-gradient(90deg,rgba(0,0,0,.7),#000 60%)}
.edge-right{-webkit-mask-image:linear-gradient(270deg,rgba(0,0,0,.7),#000 60%);mask-image:linear-gradient(270deg,rgba(0,0,0,.7),#000 60%)}

.categories{top:706px;height:529px;background:#111}
.cat-card{position:absolute;top:151px;width:212px}
.cat-img{width:212px;height:211px;border-radius:3px}
.cat-card span{display:block;margin-top:21px;text-align:center;font-size:17.5px;white-space:nowrap}

.dots{position:absolute;left:0;width:1200px;display:flex;justify-content:center;gap:11px}
.dots i{width:5px;height:5px;border-radius:50%;background:#777;display:block}
.dots i.on{background:var(--green);width:7px;height:7px;margin-top:-1px}

.trust{top:1235px;height:119px;background:var(--strip)}
.trust-item{position:absolute;top:32px}
.trust-item svg{position:absolute;left:0;top:10px}
.trust-item h3{font-size:20.5px;font-weight:500;margin-left:59px}
.trust-item p{font-size:15px;color:#dcdcdc;font-weight:300;margin-left:59px;margin-top:4px}

.products{height:747px}
.bestsellers{top:1354px;background:#111}
.featured{top:2101px;background:#1a1a1a}
.product-card{position:absolute;top:180px;width:283px;height:443px;border:1px solid var(--line);background:var(--card);border-radius:3px;overflow:hidden}
.product-img{height:196px}
.product-body{padding:24px 16px 0}
.product-body h4{font-size:16px;font-weight:400;line-height:28px;white-space:nowrap}
.rating{display:flex;align-items:center;gap:4px;margin-top:12px;font-size:12.5px;color:#ddd}
.rating span{margin-left:6px}
.price{margin-top:18px;font-size:21px;font-weight:500;display:flex;align-items:baseline;gap:10px}
.price s{font-size:13px;color:#aaa;font-weight:300}
.add-cart{margin-top:24px;height:42px;background:#1f1f1f;display:flex;align-items:center;justify-content:center;gap:8px;font-size:13px;color:#e6e6e6;border-radius:2px}
.add-cart.outline{border:1.5px solid var(--green);background:transparent}

.reviews{top:2848px;height:493px;background:linear-gradient(180deg,#121212,#1c1c1c)}
.review-card{position:absolute;top:156px;width:334px;height:207px;background:#161616;box-shadow:0 0 0 1px #242424,6px 6px 14px rgba(0,0,0,.5);padding:40px 28px}
.review-card p{font-size:13.5px;line-height:25px;color:#e6e6e6;margin-top:18px;white-space:nowrap}
.review-card b{display:block;margin-top:17px;font-size:13.5px;font-weight:600}

.site-footer{top:3341px;height:349px;background:#141414}
.footer-brand{left:141px;top:96px;font-size:24px;font-weight:600;letter-spacing:1px;display:flex;align-items:center;gap:10px}
.footer-brand .mark{width:20px;height:20px;background:#fff}
.follow{left:141px;top:222px;display:flex;align-items:center;gap:10px;font-size:13px}
.social{width:25px;height:25px;border-radius:50%;background:#2a2a2a}
.social.g{background:var(--green)}
.foot-col h5{font-size:15px;font-weight:500;color:var(--green);margin-bottom:20px}
.foot-col a{display:block;font-size:12px;color:#ddd;margin-bottom:14px;font-weight:300}
.foot-col p{font-size:12px;color:#ddd;line-height:21px;font-weight:300;margin-bottom:12px}
.newsletter{left:769px;top:54px;width:290px;height:233px;background:#1c1c1c;border-radius:6px;padding:35px 27px}
.newsletter h5{font-size:16px;font-weight:500}
.newsletter p{font-size:11px;color:#ccc;margin-top:9px;font-weight:300}
.nl-input{margin-top:27px;width:218px;height:36px;background:#fff;border-radius:18px;color:#777;font-size:12px;padding:10px 22px;position:relative}
.nl-input svg{position:absolute;right:18px;top:12px}
.nl-btn{margin-top:17px;width:151px;height:36px;background:var(--green);border-radius:18px;display:flex;align-items:center;justify-content:center;gap:18px;font-size:13px}
.copyright{top:3690px;height:53px;background:#0c0c0c;text-align:center;font-size:12px;color:#ccc;padding-top:19px;font-weight:300}
</style>
</head>
<body>
<div class="page">

<header class="site-header">
  <div class="abs brand"><span class="mark"></span>INKFORGE HUB</div>
  <div class="abs search">Search...
    <svg width="14" height="14" viewBox="0 0 24 24" fill="none" stroke="#888" stroke-width="2"><circle cx="10" cy="10" r="7"/><path d="M15 15l6 6"/></svg>
  </div>
  <div class="abs account">
    <svg width="16" height="16" viewBox="0 0 24 24" fill="none" stroke="#fff" stroke-width="1.8"><circle cx="12" cy="8" r="4"/><path d="M4 21c1-4.5 4-7 8-7s7 2.5 8 7"/></svg>Account
  </div>
  <div class="abs cart-info">10 item(s) - R150</div>
  <div class="abs cart-btn">
    <svg width="16" height="16" viewBox="0 0 24 24" fill="none" stroke="#fff" stroke-width="2"><path d="M2 4h3l2.5 11h11L21 7H6"/><circle cx="9" cy="19" r="1.5"/><circle cx="17" cy="19" r="1.5"/></svg>
  </div>
</header>

<nav class="main-nav">
  <a class="active" style="left:144px">Home</a>
  <a style="left:212px">Shop</a>
  <a style="left:275px">Tattoo Machines</a>
  <a style="left:402px">Needles &amp; Cartridges</a>
  <a style="left:558px">Hygiene &amp; Aftercare</a>
  <a style="left:709px">Accessories</a>
  <a style="left:809px">Brands</a>
  <a style="left:883px">B2B / Wholesale</a>
  <a style="left:1013px">Contact</a>
</nav>

<section class="hero">
  <div class="hero-photo" role="img" aria-label="Close-up photo of a tattoo machine needle working on skin"></div>
  <h1>Professional<br><span class="b">Tattoo Equipment<br>&amp; Supplies</span></h1>
  <p>Professional machines, inks, needles &amp; hygiene products<br>trusted by top studios nationwide.</p>
  <div class="btn btn-green" style="left:144px;top:440px;width:135px;height:45px">Shop Now</div>
  <div class="btn btn-ghost" style="left:292px;top:440px;width:176px;height:45px">B2B Wholesale</div>
</section>

<section class="categories">
  <h2 class="section-title" style="top:84px">Shop By Category</h2>
  <div class="cat-card" style="left:-94px"><div class="cat-img tone-cups edge-left" role="img" aria-label="Ink cups accessories product photo"></div><span>Accessories</span></div>
  <div class="cat-card" style="left:141px"><div class="cat-img tone-silver" role="img" aria-label="Steel cartridge grips product photo"></div><span>Cartridges</span></div>
  <div class="cat-card" style="left:376px"><div class="cat-img tone-blue" role="img" aria-label="Blue needle cartridge product photo"></div><span>Needles</span></div>
  <div class="cat-card" style="left:612px"><div class="cat-img tone-red" role="img" aria-label="Red rotary tattoo machine product photo"></div><span>Tattoo Machines</span></div>
  <div class="cat-card" style="left:847px"><div class="cat-img tone-ink-box" role="img" aria-label="Black ink bottle and box product photo"></div><span>Inks</span></div>
  <div class="cat-card" style="left:1082px"><div class="cat-img tone-stand edge-right" role="img" aria-label="Studio stand equipment product photo"></div><span>Studio Equipment</span></div>
  <div class="dots" style="top:444px"><i></i><i></i><i class="on"></i><i></i><i></i></div>
</section>

<section class="trust">
  <div class="trust-item" style="left:141px">
    <svg width="40" height="40" viewBox="0 0 40 40" fill="none" stroke="#fff" stroke-width="2"><circle cx="20" cy="20" r="18"/><path d="M12 20l6 6 11-12"/></svg>
    <h3>Secure Payments</h3><p>Our website uses SSL</p>
  </div>
  <div class="trust-item" style="left:460px">
    <svg width="40" height="40" viewBox="0 0 40 40" fill="none" stroke="#fff" stroke-width="2"><circle cx="20" cy="20" r="18"/><path d="M12 20l6 6 11-12"/></svg>
    <h3>Fast Shipping</h3><p>We ship the same day</p>
  </div>
  <div class="trust-item" style="left:776px">
    <svg width="40" height="40" viewBox="0 0 40 40" fill="none" stroke="#fff" stroke-width="2"><circle cx="20" cy="20" r="18"/><path d="M12 20l6 6 11-12"/></svg>
    <h3>Extensive stock range</h3><p>All products in stock</p>
  </div>
</section>

<svg width="0" height="0" style="position:absolute">
  <defs>
    <symbol id="star" viewBox="0 0 24 24"><path fill="#f2a516" d="M12 2l2.9 6.9 7.1.6-5.4 4.7 1.6 7.1L12 17.6 5.8 21.3l1.6-7.1L2 9.5l7.1-.6z"/></symbol>
    <symbol id="cart" viewBox="0 0 24 24"><path fill="none" stroke="#fff" stroke-width="2" d="M2 4h3l2.5 11h11L21 7H6"/><circle cx="9" cy="19" r="1.5" fill="#fff"/><circle cx="17" cy="19" r="1.5" fill="#fff"/></symbol>
    <symbol id="stars" viewBox="0 0 95 15"><use href="#star" x="0" width="15" height="15"/><use href="#star" x="20" width="15" height="15"/><use href="#star" x="40" width="15" height="15"/><use href="#star" x="60" width="15" height="15"/><use href="#star" x="80" width="15" height="15"/></symbol>
  </defs>
</svg>

<section class="products bestsellers">
  <h2 class="section-title" style="top:78px">Bestsellers</h2>
  <p class="section-sub" style="top:130px">At InkForgeHub we like to ensure that the tattoo industry standards are maintained.</p>

  <div class="product-card" style="left:-177px"><div class="product-img tone-caps edge-left" role="img" aria-label="Black ink caps product photo"></div><div class="product-body"><h4>Ember Tattoo Ink Deep<br>Purple 1oz - Ember Tattoo Ink</h4><div class="rating"><svg width="95" height="15"><use href="#stars"/></svg><span>(4.8)</span></div><div class="price">$ 1,550 <s>$ 2,560</s></div><div class="add-cart">Add to cart <svg width="15" height="15"><use href="#cart"/></svg></div></div></div>

  <div class="product-card" style="left:141px"><div class="product-img tone-purple" role="img" aria-label="Purple ink bottle product photo"></div><div class="product-body"><h4>Ember Tattoo Ink Deep<br>Purple 1oz - Ember Tattoo Ink</h4><div class="rating"><svg width="95" height="15"><use href="#stars"/></svg><span>(4.8)</span></div><div class="price">$ 2,500 <s>$ 2,560</s></div><div class="add-cart">Add to cart <svg width="15" height="15"><use href="#cart"/></svg></div></div></div>

  <div class="product-card" style="left:459px"><div class="product-img tone-caps" role="img" aria-label="Black ink caps product photo"></div><div class="product-body"><h4>Ember Tattoo Ink Deep<br>Purple 1oz - Ember Tattoo Ink</h4><div class="rating"><svg width="95" height="15"><use href="#stars"/></svg><span>(4.8)</span></div><div class="price">$ 1,550 <s>$ 2,560</s></div><div class="add-cart outline">Add to cart <svg width="15" height="15"><use href="#cart"/></svg></div></div></div>

  <div class="product-card" style="left:777px"><div class="product-img tone-black" role="img" aria-label="Black ink bottle product photo"></div><div class="product-body"><h4>Ember Tattoo Ink Deep<br>Purple 1oz - Ember Tattoo Ink</h4><div class="rating"><svg width="95" height="15"><use href="#stars"/></svg><span>(4.8)</span></div><div class="price">$ 2,500 <s>$ 2,560</s></div><div class="add-cart">Add to cart <svg width="15" height="15"><use href="#cart"/></svg></div></div></div>

  <div class="product-card" style="left:1094px"><div class="product-img tone-caps edge-right" role="img" aria-label="Black ink caps product photo"></div><div class="product-body"><h4>Ember Tattoo Ink Deep<br>Purple 1oz - Ember Tattoo Ink</h4><div class="rating"><svg width="95" height="15"><use href="#stars"/></svg><span>(4.8)</span></div><div class="price">$ 1,550 <s>$ 2,560</s></div><div class="add-cart">Add to cart <svg width="15" height="15"><use href="#cart"/></svg></div></div></div>

  <div class="dots" style="top:659px"><i></i><i></i><i class="on"></i><i></i><i></i></div>
</section>

<section class="products featured">
  <h2 class="section-title" style="top:78px">Featured Products</h2>
  <p class="section-sub" style="top:133px">At InkForgeHub we like to ensure that the tattoo industry standards are maintained.</p>

  <div class="product-card" style="left:-177px"><div class="product-img tone-stand edge-left" role="img" aria-label="Studio stand product photo"></div><div class="product-body"><h4>Ember Tattoo Ink Deep<br>Purple 1oz - Ember Tattoo Ink</h4><div class="rating"><svg width="95" height="15"><use href="#stars"/></svg><span>(4.8)</span></div><div class="price">$ 1,550 <s>$ 2,560</s></div><div class="add-cart">Add to cart <svg width="15" height="15"><use href="#cart"/></svg></div></div></div>

  <div class="product-card" style="left:141px"><div class="product-img tone-silver" role="img" aria-label="Steel grips product photo"></div><div class="product-body"><h4>Ember Tattoo Ink Deep<br>Purple 1oz - Ember Tattoo Ink</h4><div class="rating"><svg width="95" height="15"><use href="#stars"/></svg><span>(4.8)</span></div><div class="price">$ 2,500 <s>$ 2,560</s></div><div class="add-cart">Add to cart <svg width="15" height="15"><use href="#cart"/></svg></div></div></div>

  <div class="product-card" style="left:459px"><div class="product-img tone-blue" role="img" aria-label="Blue needle cartridge product photo"></div><div class="product-body"><h4>Ember Tattoo Ink Deep<br>Purple 1oz - Ember Tattoo Ink</h4><div class="rating"><svg width="95" height="15"><use href="#stars"/></svg><span>(4.8)</span></div><div class="price">$ 1,550 <s>$ 2,560</s></div><div class="add-cart outline">Add to cart <svg width="15" height="15"><use href="#cart"/></svg></div></div></div>

  <div class="product-card" style="left:777px"><div class="product-img tone-red" role="img" aria-label="Red rotary tattoo machine product photo"></div><div class="product-body"><h4>Ember Tattoo Ink Deep<br>Purple 1oz - Ember Tattoo Ink</h4><div class="rating"><svg width="95" height="15"><use href="#stars"/></svg><span>(4.8)</span></div><div class="price">$ 2,500 <s>$ 2,560</s></div><div class="add-cart">Add to cart <svg width="15" height="15"><use href="#cart"/></svg></div></div></div>

  <div class="product-card" style="left:1094px"><div class="product-img tone-ink-box edge-right" role="img" aria-label="Black ink bottle product photo"></div><div class="product-body"><h4>Ember Tattoo Ink Deep<br>Purple 1oz - Ember Tattoo Ink</h4><div class="rating"><svg width="95" height="15"><use href="#stars"/></svg><span>(4.8)</span></div><div class="price">$ 1,550 <s>$ 2,560</s></div><div class="add-cart">Add to cart <svg width="15" height="15"><use href="#cart"/></svg></div></div></div>

  <div class="dots" style="top:659px"><i></i><i></i><i class="on"></i><i></i><i></i></div>
</section>

<section class="reviews">
  <h2 class="section-title" style="top:82px">Customer Reviews</h2>
  <div class="review-card" style="left:-116px"><svg width="26" height="20" viewBox="0 0 26 20"><path fill="#3fb54d" d="M0 20V11C0 4 4 1 10 0v4c-3 1-5 3-5 6h5v10zM15 20V11c0-7 4-10 10-11v4c-3 1-5 3-5 6h5v10z"/></svg><p>Lorem Ipsum has been the industry's fact<br>that standard dummy text ever since the.</p><b>~ J.M., Cape Town</b></div>
  <div class="review-card" style="left:247px"><svg width="26" height="20" viewBox="0 0 26 20"><path fill="#3fb54d" d="M0 20V11C0 4 4 1 10 0v4c-3 1-5 3-5 6h5v10zM15 20V11c0-7 4-10 10-11v4c-3 1-5 3-5 6h5v10z"/></svg><p>Lorem Ipsum has been the industry's fact<br>that standard dummy text ever since the.</p><b>~ A.B., Chicago</b></div>
  <div class="review-card" style="left:617px"><svg width="26" height="20" viewBox="0 0 26 20"><path fill="#3fb54d" d="M0 20V11C0 4 4 1 10 0v4c-3 1-5 3-5 6h5v10zM15 20V11c0-7 4-10 10-11v4c-3 1-5 3-5 6h5v10z"/></svg><p>Lorem Ipsum has been the industry's fact<br>that standard dummy text ever since the.</p><b>~ T.T., Denver</b></div>
  <div class="review-card" style="left:988px"><svg width="26" height="20" viewBox="0 0 26 20"><path fill="#3fb54d" d="M0 20V11C0 4 4 1 10 0v4c-3 1-5 3-5 6h5v10zM15 20V11c0-7 4-10 10-11v4c-3 1-5 3-5 6h5v10z"/></svg><p>Lorem Ipsum has been the industry's fact<br>that standard dummy text ever since the.</p><b>~ C.D., Austin</b></div>
  <div class="dots" style="top:399px"><i></i><i></i><i class="on"></i><i></i><i></i></div>
</section>

<footer class="site-footer">
  <div class="abs footer-brand"><span class="mark"></span>INKFORGE HUB</div>
  <div class="abs follow">Follow Us:
    <span class="social" aria-label="Social link"></span><span class="social g" aria-label="Social link"></span><span class="social" aria-label="Social link"></span>
  </div>
  <div class="abs foot-col" style="left:398px;top:82px">
    <h5>Quick Links</h5>
    <a>Home</a><a>Shop</a><a>Shop by Category</a><a>BESTSELLERS</a><a>FEATURED PRODUCTS</a>
  </div>
  <div class="abs foot-col" style="left:577px;top:82px">
    <h5>Contact Info</h5>
    <p>InkForgeHub Pty Ltd Po Box<br>10432 Northvale 0099</p>
    <p>Email Address :<br>info@inkforgehub.com</p>
    <p>Phone Number :<br>0825550147</p>
  </div>
  <div class="abs newsletter">
    <h5>Stay in Touch</h5>
    <p>Join our newsletter to get wellness tips,</p>
    <div class="nl-input">Email address
      <svg width="14" height="11" viewBox="0 0 14 11" fill="none" stroke="#888" stroke-width="1.3"><rect x=".7" y=".7" width="12.6" height="9.6"/><path d="M1 1l6 5 6-5"/></svg>
    </div>
    <div class="nl-btn">Subscribe <svg width="12" height="12" viewBox="0 0 12 12"><path fill="#fff" d="M1 0l11 6-11 6z"/></svg></div>
  </div>
</footer>

<footer class="copyright">© 2025 Inkforge Hub. All rights reserved.</footer>

</div>
</body>
</html>
```